Letterhead and matching envelope design for a dental office

We need a new stationary design, letterhead and envelope #10, for a dental office in Denver area. We are called Brightfield Dental. We want a simple and minimalistic design but not a boring design. I wish to have one good point that makes it look professional. I have attached our logo. Feel free to use either one. I want the design for letterhead and envelope look like a "matching pair" but not look the same. The envelope doesn't have to be white and it will have an address window on bottom left.

Target Market(s)

everyone who visits dentist (adults)

Industry/Entity Type

Dental

Font styles to use
Other font styles liked:
• close to font on logo or something that matches well

Requirements
Must have
• professional
• simple, minimalistic
• unique point that stands out
Nice to have
• matching but not same design for letterhead and envelope
Should not have
• not look like all the other boring designs
• no flowery, distracting feats

```html
<!DOCTYPE html>
<html lang="en">
<head>
<meta charset="utf-8">
<title>Brightfield Dental – Stationery</title>
<link href="https://fonts.googleapis.com/css2?family=Cinzel:wght@600&family=Montserrat:wght@400&display=swap" rel="stylesheet">
<style>
  :root {
    --brand-green: #45b649;
    --paper: #ffffff;
    --backdrop: #d1d3d4;
  }
  html, body { margin: 0; padding: 0; overflow: hidden; }
  body { width: 1200px; height: 927px; background: var(--backdrop); position: relative; }
  .sheet { position: absolute; box-sizing: border-box; }
  .brand-name {
    font-family: "Cinzel", Georgia, serif;
    font-weight: 600;
    letter-spacing: 0.06em;
    white-space: nowrap;
  }
  .contact {
    font-family: "Montserrat", Arial, sans-serif;
    font-weight: 400;
    white-space: nowrap;
  }

  /* Letterhead */
  .letterhead { left: 173px; top: 67px; width: 411px; height: 531px; background: var(--paper); }
  .letterhead__brand {
    position: absolute; left: 16px; top: 66px; width: 210px;
    color: var(--brand-green); font-size: 12px;
    display: flex; align-items: center; justify-content: center; gap: 6px;
  }
  .brand-dot { width: 8px; height: 8px; border-radius: 50%; background: var(--brand-green); display: inline-block; }
  .letterhead__contact {
    position: absolute; right: 17px; top: 38px; text-align: right;
    color: var(--brand-green); font-size: 9px; line-height: 12px; font-style: normal;
  }
  .letterhead__contact .gap { height: 4px; }
  .letterhead__contact svg { vertical-align: -1px; margin-left: 5px; }
  .letterhead__rule { position: absolute; left: 0; right: 0; top: 94px; height: 1.5px; background: var(--brand-green); }

  /* Seal wordmark on green pieces */
  .seal {
    position: absolute; transform: translate(-50%, -50%);
    color: var(--paper); text-align: center;
  }
  .seal span { display: block; letter-spacing: 0.3em; padding-left: 0.3em; }

  /* Folder cover */
  .folder { left: 616px; top: 67px; width: 411px; height: 531px; background: var(--brand-green); }
  .folder .seal { left: 205px; top: 265px; font-size: 21px; line-height: 38px; }
  .folder__address {
    position: absolute; left: 0; right: 0; top: 497px; text-align: center;
    color: var(--paper); font-size: 9.5px;
  }

  /* White envelope */
  .envelope-white { left: 122px; top: 626px; width: 465px; height: 233px; background: var(--paper); }
  .envelope-white__flap {
    position: absolute; left: 0; right: 0; top: 0; height: 24px;
    background: var(--brand-green); border-radius: 12px 12px 0 0;
  }
  .envelope-white__brand {
    position: absolute; left: 0; right: 0; top: 143px; text-align: center;
    color: var(--brand-green); font-size: 14.5px;
  }
  .envelope-white__address {
    position: absolute; left: 0; right: 0; top: 210px; text-align: center;
    color: var(--brand-green); font-size: 12px;
  }

  /* Green envelope */
  .envelope-green { left: 613px; top: 650px; width: 465px; height: 209px; background: var(--brand-green); }
  .envelope-green__flap {
    position: absolute; left: 0; right: 0; top: 0; height: 22px;
    background: var(--paper); border-radius: 0 0 12px 12px;
  }
  .envelope-green .seal { left: 230px; top: 116px; font-size: 12px; line-height: 22px; }
</style>
</head>
<body>

  <section class="sheet letterhead" aria-label="Letterhead">
    <div class="letterhead__brand brand-name"><span class="brand-dot"></span>Brightfield Dental</div>
    <address class="letterhead__contact contact">
      <div>PO BOX 4410</div>
      <div>Corrin Vale 5231</div>
      <div class="gap"></div>
      <div>+330 2481-3095<svg width="7" height="8" viewBox="0 0 7 8"><path d="M1.5 0.5 L3 2.3 L2.2 3.2 Q3 5 4.6 5.8 L5.5 5 L6.7 6.5 L5.6 7.6 Q2.5 7 0.5 2 Z" fill="none" stroke="var(--brand-green)" stroke-width="0.9"/></svg></div>
      <div>info@brightfieldoffice.com<svg width="7" height="6" viewBox="0 0 7 6"><rect x="0.5" y="0.5" width="6" height="5" fill="none" stroke="var(--brand-green)" stroke-width="0.9"/><path d="M0.5 0.8 L3.5 3.2 L6.5 0.8" fill="none" stroke="var(--brand-green)" stroke-width="0.9"/></svg></div>
    </address>
    <div class="letterhead__rule"></div>
  </section>

  <section class="sheet folder" aria-label="Folder cover">
    <div class="seal brand-name"><span>Brightfield</span><span>Dental</span></div>
    <div class="folder__address contact">PO BOX 4410 Corrin Vale 5231</div>
  </section>

  <section class="sheet envelope-white" aria-label="White envelope">
    <div class="envelope-white__flap"></div>
    <div class="envelope-white__brand brand-name">Brightfield Dental</div>
    <div class="envelope-white__address contact">PO BOX 4410 Corrin Vale 5231</div>
  </section>

  <section class="sheet envelope-green" aria-label="Green envelope">
    <div class="envelope-green__flap"></div>
    <div class="seal brand-name"><span>Brightfield</span><span>Dental</span></div>
  </section>

</body>
</html>
```